TIDEWELL NUTRITION WEBSITE DESIGN

We need a full design for the website to present the company to customers and partners.
We are ' Tidewell nutrition" based in New York. We develop Multivitamins, minerals and nutritional supplements to support immunity, general health and longevity. Our products include: Pregnancy supplements, Bone supplements and Iron supplements.
The design should convey trust, natural, health and growth, also relating to the different products that we sell.

I can not download the edited design and the designer didnt submit the last revised version yet.

```html
<!DOCTYPE html>
<html lang="en">
<head>
<meta charset="utf-8">
<title>Tidewell Nutrition</title>
<link rel="stylesheet" href="https://fonts.googleapis.com/css2?family=Playfair+Display:wght@400;700;800&family=Josefin+Sans:wght@400;600&family=Montserrat:wght@400;500;600;700&display=swap">
<style>
:root{
  --green:#7cc42c;
  --green-dark:#5ea51a;
  --ink:#1f1f1f;
  --text:#3a3a3a;
  --muted:#6b6b6b;
  --soft:#f3f5ef;
  --line:#9a9a9a;
  --purple:#7c4e96;
  --blue:#0b47b6;
  --red:#cc0a0a;
}
*{margin:0;padding:0;box-sizing:border-box}
html,body{width:1200px;height:3333px;overflow:hidden;background:#fff}
body{position:relative;font-family:"Josefin Sans",sans-serif;color:var(--text)}
.abs{position:absolute}
.bg-circle{position:absolute;border-radius:50%;background:var(--soft)}
.logo{display:flex;align-items:center;gap:10px;font-family:"Montserrat",sans-serif;font-weight:500;color:var(--ink)}
.logo-dot{width:22px;height:22px;border-radius:50%;background:var(--green)}
.nav{top:34px;left:647px;display:flex;gap:0;font-family:"Montserrat",sans-serif;font-size:11px;letter-spacing:.2px;color:var(--ink)}
.nav a{position:absolute;top:0;white-space:nowrap;text-decoration:none;color:var(--ink)}
.nav a.active{color:var(--green)}
.eyebrow{font-family:"Montserrat",sans-serif;font-size:16px;color:var(--ink)}
.hero-title{font-family:"Playfair Display",serif;font-weight:800;font-size:44px;color:var(--ink);white-space:nowrap}
.hero-title span{color:var(--green)}
.para{font-size:13.5px;line-height:20.3px;color:var(--text)}
.btn{position:absolute;width:118px;height:30px;border:1.5px solid var(--ink);border-radius:8px;overflow:hidden;background:#fff;font-family:"Montserrat",sans-serif;font-weight:700;font-size:9.5px;color:var(--ink);display:flex;align-items:center}
.btn .label{flex:1;text-align:center;padding-right:2px}
.btn .arrow{width:25px;height:100%;background:var(--green);display:flex;align-items:center;justify-content:center}
.btn .arrow i{width:0;height:0;border-left:6px solid #fff;border-top:4px solid transparent;border-bottom:4px solid transparent}
.section-title{font-family:"Playfair Display",serif;font-size:25px;color:var(--ink);white-space:nowrap}
.section-title.lg{font-size:36px}
.rule{position:absolute;height:1.5px;background:var(--green)}
.card{position:absolute;top:593px;width:194px;height:255px;background:#fff;border-radius:8px;box-shadow:0 2px 12px rgba(0,0,0,.12);text-align:center}
.card svg{position:absolute;top:34px;left:72px}
.card h3{position:absolute;top:97px;width:100%;font-family:"Montserrat",sans-serif;font-weight:500;font-size:16px;color:var(--ink)}
.card p{position:absolute;top:127px;left:12px;right:12px;font-size:11px;line-height:15.5px;color:var(--muted)}
.card .go{position:absolute;top:203px;left:88px;width:18px;height:18px;border-radius:50%;background:var(--green);display:flex;align-items:center;justify-content:center}
.card .go i{width:0;height:0;border-left:5px solid #fff;border-top:3.5px solid transparent;border-bottom:3.5px solid transparent;margin-left:2px}
.product-visual{position:absolute;width:460px;height:301px;border-radius:10px;box-shadow:0 6px 16px rgba(0,0,0,.18)}
.product-visual.purple{background:linear-gradient(135deg,#8a5aa3,var(--purple))}
.product-visual.blue{background:linear-gradient(135deg,#1456c8,var(--blue))}
.product-visual.red{background:linear-gradient(135deg,#d81818,var(--red))}
.field-label{position:absolute;font-family:"Montserrat",sans-serif;font-size:12px;color:var(--ink)}
.field-line{position:absolute;height:1px;background:var(--line)}
.submit{position:absolute;left:527px;top:2781px;width:147px;height:41px;border-radius:21px;background:var(--green);color:#fff;font-family:"Montserrat",sans-serif;font-weight:700;font-size:12px;letter-spacing:1px;display:flex;align-items:center;justify-content:center}
.footer{position:absolute;left:0;top:2959px;width:1200px;height:374px;background:var(--soft)}
.foot-head{position:absolute;top:3012px;font-family:"Playfair Display",serif;font-size:16px;color:var(--ink)}
.foot-list{position:absolute;top:3050px;list-style:none;font-size:10.5px;color:var(--text)}
.foot-list li{height:22.6px}
.vdiv{position:absolute;top:3015px;width:1px;height:150px;background:#d6d9d0}
.social{position:absolute;top:3163px;width:30px;height:30px;border-radius:50%;border:1.5px solid var(--green)}
.contact-row{position:absolute;left:884px;display:flex;align-items:flex-start;gap:10px;font-size:10.5px;line-height:13px;color:var(--text)}
.contact-icon{flex:none;width:25px;height:25px;border-radius:50%;background:var(--green);display:flex;align-items:center;justify-content:center}
.copyright{position:absolute;top:3268px;width:1200px;text-align:center;font-size:10.5px;color:var(--ink)}
.copyright span{color:var(--green)}
</style>
</head>
<body>

<!-- soft background shapes -->
<div class="bg-circle" style="left:-430px;top:520px;width:920px;height:1400px"></div>
<div class="bg-circle" style="left:840px;top:1210px;width:560px;height:440px"></div>
<div class="bg-circle" style="left:354px;top:2446px;width:492px;height:492px"></div>

<!-- header -->
<div class="abs logo" style="left:130px;top:26px;font-size:20px"><span class="logo-dot"></span>Tidewell Nutrition</div>
<nav class="abs nav">
  <a class="active" style="left:0">HOME</a>
  <a style="left:75px">ABOUT US</a>
  <a style="left:169px">SERVICES</a>
  <a style="left:256px">PRODUCTS</a>
  <a style="left:355px">CONTACT US</a>
</nav>

<!-- hero -->
<div class="abs eyebrow" style="left:130px;top:205px">Welcome To</div>
<h1 class="abs hero-title" style="left:130px;top:223px">Our <span>New</span> Lifestyle</h1>
<p class="abs para" style="left:130px;top:294px;width:380px">Sed ut perspiciatis unde omnis iste natus error sit voluptatem accusantium doloremque</p>
<div class="btn" style="left:130px;top:357px"><span class="label">GET STARTED</span><span class="arrow"><i></i></span></div>
<div class="abs" role="img" aria-label="Green leaf swirl with a wellness photo inside the leaves, behind three supplement bottles" style="left:560px;top:70px;width:514px;height:473px;border-radius:50% 40% 30% 50%;background:radial-gradient(circle at 40% 40%,#8fcf3a 0%,#5f9b25 45%,#eef1ea 75%,rgba(255,255,255,0) 100%)"></div>

<!-- intro -->
<h2 class="abs section-title lg" style="left:130px;top:625px">Tempora Incidunt</h2>
<div class="rule" style="left:130px;top:676px;width:272px"></div>
<p class="abs para" style="left:130px;top:706px;width:312px">Sed ut perspiciatis unde omnis iste natus error sit voluptatem accusantium doloremque laudantium, totam rem aperiam, eaque ipsa quae ab illo inventore veritatis et quasi architecto beatae vitae dicta sunt explicabo.</p>

<div class="card" style="left:449px">
  <svg width="50" height="50" viewBox="0 0 50 50" fill="none" stroke-width="2" stroke-linejoin="round">
    <path d="M14 18c0-8 6-12 10-12M22 18c2-7 8-10 12-9M30 18c0-5 4-8 8-8" stroke="#7cc42c"/>
    <path d="M6 20h38l-4 22H10z" stroke="#1f1f1f"/>
    <path d="M16 26v10M22 26v10M28 26v10M34 26v10" stroke="#1f1f1f"/>
  </svg>
  <h3>Exercitationem</h3>
  <p>No one rejects, dislikes, or avoids pleasure itself, because it is pleasure, but because those who do not know how to pursue...</p>
  <span class="go"><i></i></span>
</div>
<div class="card" style="left:663px">
  <svg width="50" height="50" viewBox="0 0 50 50" fill="none" stroke-width="2" stroke-linejoin="round" stroke-linecap="round">
    <rect x="10" y="8" width="26" height="36" rx="2" stroke="#1f1f1f"/>
    <rect x="17" y="5" width="12" height="6" rx="1" stroke="#1f1f1f"/>
    <path d="M14 19l2 2 4-4M14 28l2 2 4-4M23 19h9M23 28h9M14 37h8" stroke="#7cc42c"/>
    <circle cx="37" cy="38" r="5" stroke="#7cc42c"/>
  </svg>
  <h3>Nutration</h3>
  <p>No one rejects, dislikes, or avoids pleasure itself, because it is pleasure, but because those who do not know how to pursue...</p>
  <span class="go"><i></i></span>
</div>
<div class="card" style="left:876px">
  <svg width="50" height="50" viewBox="0 0 50 50" fill="none" stroke-width="2" stroke-linejoin="round" stroke-linecap="round">
    <rect x="19" y="12" width="12" height="16" rx="2" stroke="#1f1f1f"/>
    <path d="M21 9h8" stroke="#1f1f1f"/>
    <path d="M12 18V8M8 12l4-4 4 4M38 18V8M34 12l4-4 4 4" stroke="#7cc42c"/>
    <path d="M6 36l8-4h10c2 0 2 3 0 3h-6M14 42h14l12-8c2-1 0-4-2-3l-8 4" stroke="#1f1f1f"/>
  </svg>
  <h3>Quisquam</h3>
  <p>No one rejects, dislikes, or avoids pleasure itself, because it is pleasure, but because those who do not know how to pursue...</p>
  <span class="go"><i></i></span>
</div>

<!-- pregnancy -->
<div class="product-visual purple" role="img" aria-label="Three white pregnancy supplement bottles on a purple background" style="left:130px;top:906px"></div>
<h2 class="abs section-title" style="left:723px;top:940px">Pregnancy Supplements</h2>
<div class="rule" style="left:723px;top:973px;width:252px"></div>
<p class="abs para" style="left:723px;top:996px;width:352px">Sed ut perspiciatis unde omnis iste natus error sit voluptatem accusantium doloremque laudantium, totam rem aperiam, eaque ipsa quae ab illo inventore veritatis et quasi architecto beatae vitae dicta sunt explicabo &nbsp;enim ipsam voluptatem quia voluptas sit aspernatur aut odit aut fugit, sed quia consequuntur</p>
<div class="btn" style="left:723px;top:1139px"><span class="label">READ MORE</span><span class="arrow"><i></i></span></div>

<!-- bone -->
<h2 class="abs section-title" style="left:130px;top:1288px">Bone Supplements</h2>
<div class="rule" style="left:130px;top:1321px;width:194px"></div>
<p class="abs para" style="left:130px;top:1345px;width:352px">Sed ut perspiciatis unde omnis iste natus error sit voluptatem accusantium doloremque laudantium, totam rem aperiam, eaque ipsa quae ab illo inventore veritatis et quasi architecto beatae vitae dicta sunt explicabo &nbsp;enim ipsam voluptatem quia voluptas sit aspernatur aut odit aut fugit, sed quia consequuntur</p>
<div class="btn" style="left:130px;top:1488px"><span class="label">READ MORE</span><span class="arrow"><i></i></span></div>
<div class="product-visual blue" role="img" aria-label="Three white bone supplement bottles on a blue background" style="left:610px;top:1254px"></div>

<!-- iron -->
<div class="product-visual red" role="img" aria-label="Three white iron supplement bottles on a red background" style="left:130px;top:1602px"></div>
<h2 class="abs section-title" style="left:723px;top:1635px">Iron Supplements</h2>
<div class="rule" style="left:723px;top:1668px;width:188px"></div>
<p class="abs para" style="left:723px;top:1691px;width:352px">Sed ut perspiciatis unde omnis iste natus error sit voluptatem accusantium doloremque laudantium, totam rem aperiam, eaque ipsa quae ab illo inventore veritatis et quasi architecto beatae vitae dicta sunt explicabo &nbsp;enim ipsam voluptatem quia voluptas sit aspernatur aut odit aut fugit, sed quia consequuntur</p>
<div class="btn" style="left:723px;top:1835px"><span class="label">READ MORE</span><span class="arrow"><i></i></span></div>

<!-- about -->
<div class="abs eyebrow" style="left:130px;top:2037px">About</div>
<h2 class="abs section-title lg" style="left:130px;top:2057px">Tidewell-Nutrition</h2>
<div class="rule" style="left:130px;top:2107px;width:238px"></div>
<p class="abs para" style="left:130px;top:2135px;width:486px">Sed ut perspiciatis unde omnis iste natus error sit voluptatem accusantium doloremque laudantium, totam rem aperiam, eaque ipsa quae ab illo inventore veritatis et quasi architecto beatae vitae dicta sunt explicabo. Nemo enim ipsam voluptatem quia voluptas sit aspernatur aut odit aut fugit, sed quia consequuntur magni dolores eos qui ratione voluptatem sequi nesciunt.</p>
<div class="btn" style="left:130px;top:2263px"><span class="label">READ MORE</span><span class="arrow"><i></i></span></div>
<div class="abs" role="img" aria-label="Swirl of green leaves filled with a nature photo" style="left:673px;top:1962px;width:400px;height:406px;border-radius:50%;background:radial-gradient(circle,#fff 0%,#fff 12%,#6ea62a 30%,#4d7f1e 55%,rgba(255,255,255,0) 72%)"></div>

<!-- contact -->
<div class="abs eyebrow" style="left:0;width:1200px;text-align:center;top:2427px">Contact Us</div>
<h2 class="abs section-title" style="left:0;width:1200px;text-align:center;top:2447px;font-size:36px">Have you Any Question?</h2>
<span class="field-label" style="left:239px;top:2528px">Name:</span>
<span class="field-line" style="left:239px;top:2550px;width:353px"></span>
<span class="field-label" style="left:607px;top:2528px">Phone:</span>
<span class="field-line" style="left:607px;top:2550px;width:353px"></span>
<span class="field-label" style="left:239px;top:2597px">Email:</span>
<span class="field-line" style="left:239px;top:2619px;width:721px"></span>
<span class="field-label" style="left:239px;top:2666px">Comments:</span>
<span class="field-line" style="left:239px;top:2752px;width:721px"></span>
<div class="submit">SUBMIT</div>

<!-- footer -->
<footer class="footer"></footer>
<div class="abs logo" style="left:130px;top:3040px;font-size:34px;gap:14px"><span class="logo-dot" style="width:34px;height:34px"></span>Tidewell Nutrition</div>
<p class="abs" style="left:130px;top:3114px;width:330px;font-size:10.5px;line-height:18px;color:var(--text)">Sed ut perspiciatis unde omnis iste natus error sit voluptatem accusantium doloremque laudantium...</p>
<span class="social" style="left:131px"></span>
<span class="social" style="left:173px"></span>
<span class="social" style="left:213px"></span>

<h4 class="foot-head" style="left:510px">Quick Links</h4>
<ul class="foot-list" style="left:510px"><li>Home</li><li>About Us</li><li>Services</li><li>Products</li><li>Contact Us</li></ul>
<span class="vdiv" style="left:644px"></span>
<h4 class="foot-head" style="left:690px">Products</h4>
<ul class="foot-list" style="left:690px"><li>Pregnancy supplements</li><li>Bone supplements</li><li>ron supplements</li></ul>
<span class="vdiv" style="left:842px"></span>
<h4 class="foot-head" style="left:884px">Contacts</h4>
<div class="contact-row" style="top:3050px">
  <span class="contact-icon"><svg width="12" height="14" viewBox="0 0 12 14"><path d="M6 0a5 5 0 0 0-5 5c0 4 5 9 5 9s5-5 5-9a5 5 0 0 0-5-5zm0 7a2 2 0 1 1 0-4 2 2 0 0 1 0 4z" fill="#fff"/></svg></span>
  <span>18/B Lorem ipsum dolar sit amet<br>New York 25KL USA</span>
</div>
<div class="contact-row" style="top:3098px;align-items:center">
  <span class="contact-icon"><svg width="12" height="12" viewBox="0 0 12 12"><path d="M2.5 0.5l2 2.5-1.2 1.3c.7 1.5 1.9 2.7 3.4 3.4L8 6.5l2.5 2-1.3 2.5C4.7 10.8 1.2 7.3 0.5 2.8z" fill="#fff"/></svg></span>
  <span>+2 (555) 240 6100</span>
</div>
<div class="contact-row" style="top:3140px;align-items:center">
  <span class="contact-icon"><svg width="13" height="10" viewBox="0 0 13 10" fill="none" stroke="#fff" stroke-width="1.4"><rect x=".7" y=".7" width="11.6" height="8.6" rx="1"/><path d="M1 1.2l5.5 4.3L12 1.2"/></svg></span>
  <span>info@tidewellnutrition.com</span>
</div>

<div class="abs" style="left:130px;top:3231px;width:940px;height:1px;background:#d6d9d0"></div>
<p class="copyright">Copyright © 2022 <span>Tidewell-Nutrition</span>. All Rights Reserved.</p>

</body>
</html>
```